SkyVelour IOS App for iPhone / Luxury private aviation / 1 main screen

Hello there !

SkyVelour Ltd is a VIP aircraft operator. You can see our https://social-example.net/skyvelour page or our https://photo-example.net/sky_velour . Our web page http://skyvelour-demo.net says it all, we don't communicate much except for the music industry activities we have.

We have developed a very simple app, 6 screens total, that will give the user a distance and a flight time between any two airports of the world. Enter a departure point (New York or JFK or KJFK...) and a destination (like Los Angeles, LAX or KLAX) and we will give you the flight time depending on the type of private jet you are selecting in the aircraft database of the app.

You might want to see the attached pdf for the flow...Any design idea is welcome.

We want it to be simple, pure, fast, and of course less will be more. We should see a unity between all these screens, same design spirit of course... On the main screen of the app, we are showing:- the company logo- a departure airport- a destination airport- the selected aircraft with access to a mini photo gallery of the said airplane- a flight time shown in hours and minutes- a distance shown in Miles, Nautical Miles or KM according to the pref page selection- an access to a contact screen- an access to a parameters screen (will develop some of it on a later version).

Thanks !!

Mathis

Target Market(s)

Private aircraft travelers and VIP flights brokers

Industry/Entity Type

Aviation

Font styles to use
Sans Serif

Colors
aaaaaa
5c5c5c
1b1b1b
e9e9e9
ffffff

Requirements
Must have
• Our logo
Nice to have
• Elegant design
Should not have
• Complicated stuff

```html
<!DOCTYPE html>
<html lang="en">
<head>
<meta charset="utf-8">
<title>SkyVelour – App Screens</title>
<link href="https://fonts.googleapis.com/css2?family=Mulish:wght@300;400;600;700&display=swap" rel="stylesheet">
<style>
:root{
  --stage:#5c5c5c;
  --screen-top:#b4b4b4;
  --screen-bottom:#9c9c9c;
  --screen-dim-top:#8e8e8e;
  --screen-dim-bottom:#7d7d7d;
  --card:#3a3a3a;
  --card-dim:#2f2f2f;
  --ink:#1b1b1b;
  --bar:#1b1b1b;
  --line:#6a6a6a;
  --soft:#e9e9e9;
  --white:#ffffff;
  --brand:#3c3c3c;
  --tab-idle:#6f6f6f;
}
*{box-sizing:border-box;margin:0;padding:0}
html,body{width:1200px;height:900px;overflow:hidden}
body{background:var(--stage);font-family:"Mulish",sans-serif;color:var(--white);position:relative}
.app-title{position:absolute;top:90px;left:0;width:1200px;text-align:center;font-weight:300;font-size:46px;letter-spacing:.5px}
.screen-label{position:absolute;font-weight:300;font-size:16px;color:var(--white);white-space:nowrap}
.screen{position:absolute;overflow:hidden;background:linear-gradient(var(--screen-dim-top),var(--screen-dim-bottom))}
.screen--home{background:linear-gradient(var(--screen-top),var(--screen-bottom));border-radius:26px;box-shadow:0 6px 24px rgba(0,0,0,.35)}
.status{position:absolute;top:0;left:0;right:0;height:24px;display:flex;align-items:center;justify-content:space-between;padding:0 12px;font-size:7.5px;color:var(--ink)}
.status-icons{display:flex;gap:3px;align-items:center}
.status-icons svg{width:8px;height:6px;fill:var(--ink)}
.battery{width:10px;height:5px;border-radius:1.5px;background:var(--ink)}
.search{position:absolute;left:14px;right:0;height:14px;background:var(--ink);border-radius:2px;display:flex;align-items:center;gap:4px;padding-left:8px;font-size:6px;color:var(--soft)}
.search svg{width:6px;height:6px;stroke:var(--soft);fill:none;stroke-width:3}
.media-card{position:absolute;left:14px;right:0;background:var(--card-dim);border-radius:3px 0 0 3px;overflow:hidden}
.photo{height:86px}
.photo--airliner-blue{background:linear-gradient(170deg,#56637f 0%,#46536f 45%,#3a4660 100%)}
.photo--airliner-grey{background:linear-gradient(170deg,#646a78 0%,#575d6b 50%,#4b505c 100%)}
.photo--terminal-night{background:linear-gradient(180deg,#3b2d3a 0%,#5a3a5f 45%,#3a2f2a 75%,#2c2520 100%)}
.photo--airport-aerial{background:linear-gradient(160deg,#8a8e90 0%,#6e7274 55%,#7b8084 100%)}
.photo--runway-aerial{background:linear-gradient(180deg,#7d8784 0%,#66775c 50%,#6f7a63 100%)}
.photo--thumb{background:linear-gradient(160deg,#6a7284,#535a69)}
.pill{position:absolute;top:8px;left:10px;height:11px;padding:0 6px 0 2px;background:var(--ink);border-radius:6px;display:flex;align-items:center;gap:3px;font-size:6.5px;font-weight:700}
.pill .dot{width:8px;height:8px;border-radius:50%;background:var(--white)}
.pill .tick{width:8px;height:8px;border-radius:50%;border:1px solid var(--white);display:flex;align-items:center;justify-content:center}
.pill .tick svg{width:5px;height:5px;stroke:var(--white);fill:none;stroke-width:4}
.card-head{display:flex;justify-content:space-between;align-items:center;padding:0 0 0 9px;height:26px;font-size:6.5px;font-weight:700;letter-spacing:.2px;white-space:nowrap}
.more{background:var(--ink);border-radius:5px;font-size:4.5px;font-weight:400;padding:2px 6px;color:var(--soft);margin-right:4px}
.details{padding:0 10px 6px 16px;font-size:6.5px;letter-spacing:.3px}
.details div{display:flex;justify-content:space-between;line-height:10.2px}
.details b{font-weight:700}
.gallery{display:grid;grid-template-columns:repeat(3,54px);gap:8px;padding:4px 0 0 10px}
.gallery span{height:36px;display:block}
.tabbar{position:absolute;left:0;right:0;bottom:0;background:var(--bar);display:flex;justify-content:space-around;padding:8px 4px 0}
.tab{display:flex;flex-direction:column;align-items:center;gap:2px;font-size:6.5px;color:var(--tab-idle);width:40px}
.tab svg{width:12px;height:12px;fill:currentColor}
.tab--active{color:var(--white)}
.home-bar{position:absolute;bottom:5px;left:50%;width:110px;height:2.5px;margin-left:-55px;background:var(--white);border-radius:2px}
.brand{position:absolute;left:0;right:0;text-align:center;font-weight:400;color:var(--brand)}
.flight-card{position:absolute;left:15px;width:198px;top:142px;height:219px;background:var(--card);border-radius:3px;padding:14px 14px 0}
.flight-card h2{font-weight:400;font-size:9.5px;padding-bottom:8px;border-bottom:.5px solid var(--line)}
.leg{margin-top:10px}
.leg-title{display:flex;align-items:center;gap:6px;font-size:8px}
.leg-icon{width:20px;height:20px;border-radius:50%;background:var(--ink);display:flex;align-items:center;justify-content:center}
.leg-icon svg{width:10px;height:10px;fill:var(--white)}
.rows{margin-top:6px;font-size:6px}
.rows div{display:flex;justify-content:space-between;line-height:12px;white-space:nowrap}
.rows b{font-weight:700;letter-spacing:.3px}
.totals{margin-top:10px;padding-top:8px;border-top:.5px solid var(--line)}
.footer-note{position:absolute;top:436px;left:0;right:0;text-align:center;font-size:6.5px;color:#5e5e5e;letter-spacing:.3px}
.contact-card{position:absolute;left:0;width:188px;top:131px;height:191px;background:var(--card-dim);border-radius:0 3px 3px 0;padding:14px 14px 0 6px}
.contact-card h2,.settings-card h2{font-weight:400;font-size:9.5px;padding-bottom:8px;border-bottom:.5px solid var(--line);white-space:nowrap}
.channels{display:grid;grid-template-columns:repeat(3,46px);gap:12px 16px;margin-top:11px}
.channel{display:flex;flex-direction:column;align-items:center;gap:5px;font-size:7px;color:var(--soft)}
.channel-square{width:45px;height:45px;background:var(--ink);border-radius:4px}
.channel-round{width:45px;height:45px;border-radius:50%;background:var(--ink);display:flex;align-items:center;justify-content:center}
.channel-round svg{width:20px;height:20px;fill:var(--white)}
.settings-card{position:absolute;left:0;width:190px;top:92px;height:190px;background:var(--card-dim);border-radius:0 3px 3px 0;padding:14px 14px 0 18px}
.setting{display:flex;justify-content:space-between;align-items:center;font-size:9px;margin-top:9px}
.select{background:var(--ink);border-radius:8px;padding:3px 10px;font-weight:700;font-size:9px;display:flex;align-items:center;gap:5px}
.select i{border:3px solid transparent;border-top:4px solid var(--white);margin-top:3px}
.version{position:absolute;bottom:10px;left:0;right:0;text-align:center;font-size:7px;padding-left:18px}
</style>
</head>
<body>
<svg width="0" height="0" style="position:absolute" aria-hidden="true">
  <symbol id="i-home" viewBox="0 0 24 24"><path d="M12 3 2 12h3v9h5v-6h4v6h5v-9h3z"/></symbol>
  <symbol id="i-plane" viewBox="0 0 24 24"><path d="M12 2c.8 0 1.3.8 1.3 1.8V9l8 4.5v2l-8-2.5v5l2.2 1.6V21L12 20l-3.5 1v-1.4l2.2-1.6v-5l-8 2.5v-2l8-4.5V3.8C10.7 2.8 11.2 2 12 2z"/></symbol>
  <symbol id="i-tower" viewBox="0 0 24 24"><path d="M4 21v-8h16v8zM9 12V9h6v3zM7 8h10l-1.5-4h-7z"/></symbol>
  <symbol id="i-phone" viewBox="0 0 24 24"><path d="M6.6 10.8a15 15 0 0 0 6.6 6.6l2.2-2.2c.3-.3.7-.4 1-.2 1.1.4 2.3.6 3.6.6.6 0 1 .4 1 1V20c0 .6-.4 1-1 1C10.6 21 3 13.4 3 4c0-.6.4-1 1-1h3.5c.6 0 1 .4 1 1 0 1.3.2 2.5.6 3.6.1.3 0 .7-.2 1z"/></symbol>
  <symbol id="i-gear" viewBox="0 0 24 24"><circle cx="12" cy="12" r="8" fill="none" stroke="currentColor" stroke-width="4" stroke-dasharray="3 2.3"/><circle cx="12" cy="12" r="6.5"/><circle cx="12" cy="12" r="2.4" fill="#1b1b1b"/></symbol>
  <symbol id="i-search" viewBox="0 0 24 24"><circle cx="10" cy="10" r="6"/><path d="M15 15l6 6"/></symbol>
  <symbol id="i-tick" viewBox="0 0 24 24"><path d="M4 12l5 5 11-11"/></symbol>
  <symbol id="i-mail" viewBox="0 0 24 24"><path d="M2 5h20v14H2zM3.5 6.5 12 13l8.5-6.5z" fill-rule="evenodd"/></symbol>
  <symbol id="i-signal" viewBox="0 0 8 6"><rect x="0" y="4" width="1.5" height="2"/><rect x="2.2" y="2.8" width="1.5" height="3.2"/><rect x="4.4" y="1.4" width="1.5" height="4.6"/><rect x="6.5" y="0" width="1.5" height="6"/></symbol>
</svg>

<h1 class="app-title">SkyVelour</h1>

<p class="screen-label" style="left:137px;top:288px">Choose Aircraft</p>
<p class="screen-label" style="left:325px;top:266px">Choose Airport</p>
<p class="screen-label" style="left:553px;top:232px">Home Screen</p>
<p class="screen-label" style="left:779px;top:266px">Contact</p>
<p class="screen-label" style="left:973px;top:288px">Settings</p>

<section class="screen screen--aircraft" style="left:78px;top:326px;width:206px;height:414px">
  <div class="status"><span>9:41</span><span class="status-icons"><svg><use href="#i-signal"/></svg></span></div>
  <div class="search" style="top:27px"><svg><use href="#i-search"/></svg>Search Aircrafts</div>
  <article class="media-card" style="top:47px">
    <div class="photo photo--airliner-blue" role="img" aria-label="Photo of a wide-body airliner in flight against a blue sky"></div>
    <span class="pill"><span class="dot"></span>Select</span>
    <div class="card-head">Stratus S-270ER<span class="more">More details</span></div>
  </article>
  <article class="media-card" style="top:163px;height:206px">
    <div class="photo photo--airliner-grey" role="img" aria-label="Photo of a four-engine jumbo jet on approach"></div>
    <span class="pill"><span class="tick"><svg><use href="#i-tick"/></svg></span>Unselect</span>
    <div class="card-head">Stratus S-410<span class="more">Less details</span></div>
    <div class="gallery">
      <span class="photo--thumb" role="img" aria-label="Gallery photo: cabin interior"></span>
      <span class="photo--thumb" role="img" aria-label="Gallery photo: aircraft parked on apron"></span>
      <span class="photo--thumb" role="img" aria-label="Gallery photo: passenger seating"></span>
      <span class="photo--thumb" role="img" aria-label="Gallery photo: aircraft on taxiway"></span>
      <span class="photo--thumb" role="img" aria-label="Gallery photo: upper deck cabin"></span>
      <span class="photo--thumb" role="img" aria-label="Gallery photo: aircraft in flight"></span>
    </div>
  </article>
  <nav class="tabbar" style="height:45px">
    <span class="tab"><svg><use href="#i-home"/></svg>Home</span>
    <span class="tab tab--active"><svg><use href="#i-plane"/></svg>Aircrafts</span>
    <span class="tab"><svg><use href="#i-tower"/></svg>Airports</span>
    <span class="tab"><svg><use href="#i-phone"/></svg>Contact</span>
    <span class="tab"><svg><use href="#i-gear"/></svg>Settings</span>
  </nav>
  <span class="home-bar" style="left:70%"></span>
</section>

<section class="screen screen--airport" style="left:266px;top:308px;width:210px;height:450px">
  <div class="status"><span>9:41</span><span class="status-icons"><svg><use href="#i-signal"/></svg><span class="battery"></span></span></div>
  <div class="search" style="top:29px"><svg><use href="#i-search"/></svg>Search Airports</div>
  <article class="media-card" style="top:49px">
    <div class="photo photo--terminal-night" role="img" aria-label="Photo of an airport landmark building lit purple at night"></div>
    <span class="pill"><span class="dot"></span>Select</span>
    <div class="card-head">Pacific Crest International Airport<span class="more">More details ▾</span></div>
  </article>
  <article class="media-card" style="top:165px">
    <div class="photo photo--airport-aerial" role="img" aria-label="Aerial photo of an airport beside a bay"></div>
    <span class="pill"><span class="tick"><svg><use href="#i-tick"/></svg></span>Unselect</span>
    <div class="card-head">Bayview International Airport<span class="more">Less details ▴</span></div>
    <div class="details">
      <div><span>Elevation</span><b>13ft</b></div>
      <div><span>Address</span><b>CA, 90210 BV</b></div>
      <div><span>City</span><b>Bayview</b></div>
      <div><span>Country</span><b>USA</b></div>
      <div><span>Website</span><b>www.bayview-air.net</b></div>
    </div>
  </article>
  <article class="media-card" style="top:333px">
    <div class="photo photo--runway-aerial" role="img" aria-label="Aerial photo of runways among green fields"></div>
    <span class="pill"><span class="dot"></span>Select</span>
  </article>
  <nav class="tabbar" style="height:45px">
    <span class="tab"><svg><use href="#i-home"/></svg>Home</span>
    <span class="tab"><svg><use href="#i-plane"/></svg>Aircrafts</span>
    <span class="tab tab--active"><svg><use href="#i-tower"/></svg>Airports</span>
    <span class="tab"><svg><use href="#i-phone"/></svg>Contact</span>
    <span class="tab"><svg><use href="#i-gear"/></svg>Settings</span>
  </nav>
  <span class="home-bar"></span>
</section>

<section class="screen screen--settings" style="left:915px;top:326px;width:206px;height:414px">
  <div class="status"><span></span><span class="status-icons"><svg><use href="#i-signal"/></svg><span class="battery"></span></span></div>
  <div class="settings-card">
    <h2>Application Settings</h2>
    <div class="setting"><span>Measuring Units</span><span class="select">Metric<i></i></span></div>
    <div class="setting"><span>Other Settings</span></div>
    <p class="version">App version 1.0</p>
  </div>
  <nav class="tabbar" style="height:45px">
    <span class="tab"><svg><use href="#i-home"/></svg>Home</span>
    <span class="tab"><svg><use href="#i-plane"/></svg>Aircrafts</span>
    <span class="tab"><svg><use href="#i-tower"/></svg>Airports</span>
    <span class="tab"><svg><use href="#i-phone"/></svg>Contact</span>
    <span class="tab tab--active"><svg><use href="#i-gear"/></svg>Settings</span>
  </nav>
  <span class="home-bar" style="left:60%;width:92px"></span>
</section>

<section class="screen screen--contact" style="left:727px;top:308px;width:204px;height:450px">
  <div class="status"><span>9:41</span><span class="status-icons"><svg><use href="#i-signal"/></svg><span class="battery"></span></span></div>
  <p class="brand" style="top:92px;font-size:22px">SkyVelour</p>
  <div class="contact-card">
    <h2>Follow &amp; Contact us</h2>
    <div class="channels">
      <span class="channel"><span class="channel-square"></span>Social</span>
      <span class="channel"><span class="channel-square"></span>Photos</span>
      <span class="channel"><span class="channel-round"><svg><use href="#i-mail"/></svg></span>Email</span>
      <span class="channel"><span class="channel-round"><svg><use href="#i-phone"/></svg></span>Phone</span>
    </div>
  </div>
  <nav class="tabbar" style="height:45px">
    <span class="tab"><svg><use href="#i-home"/></svg>Home</span>
    <span class="tab"><svg><use href="#i-plane"/></svg>Aircrafts</span>
    <span class="tab"><svg><use href="#i-tower"/></svg>Airports</span>
    <span class="tab tab--active"><svg><use href="#i-phone"/></svg>Contact</span>
    <span class="tab"><svg><use href="#i-gear"/></svg>Settings</span>
  </nav>
  <span class="home-bar"></span>
</section>

<section class="screen screen--home" style="left:486px;top:282px;width:228px;height:502px">
  <div class="status" style="padding:0 18px"><span>9:41</span><span class="status-icons"><svg><use href="#i-signal"/></svg><span class="battery"></span></span></div>
  <p class="brand" style="top:92px;font-size:24px">SkyVelour</p>
  <div class="flight-card">
    <h2>Flight details</h2>
    <div class="leg">
      <div class="leg-title"><span class="leg-icon"><svg style="transform:rotate(60deg)"><use href="#i-plane"/></svg></span>Departure</div>
      <div class="rows">
        <div><span>Time</span><b>09:00 AM</b></div>
        <div><span>Departure</span><b>Bayview International Airport</b></div>
      </div>
    </div>
    <div class="leg">
      <div class="leg-title"><span class="leg-icon"><svg style="transform:rotate(120deg)"><use href="#i-plane"/></svg></span>Arrival</div>
      <div class="rows">
        <div><span>Time</span><b>02:00 PM</b></div>
        <div><span>Arrival</span><b>Eastgate International Airport</b></div>
      </div>
    </div>
    <div class="rows totals">
      <div><span>Total Time</span><b>5 Hours (estimated)</b></div>
      <div><span>Total Distance</span><b>2,500 miles</b></div>
      <div><span>Aircraft</span><b>Stratus S-270</b></div>
    </div>
  </div>
  <p class="footer-note">SkyVelour Ltd, All Rights Reserved</p>
  <nav class="tabbar" style="height:52px">
    <span class="tab tab--active"><svg><use href="#i-home"/></svg>Home</span>
    <span class="tab"><svg><use href="#i-plane"/></svg>Aircrafts</span>
    <span class="tab"><svg><use href="#i-tower"/></svg>Airports</span>
    <span class="tab"><svg><use href="#i-phone"/></svg>Contact</span>
    <span class="tab"><svg><use href="#i-gear"/></svg>Settings</span>
  </nav>
  <span class="home-bar"></span>
</section>
</body>
</html>
```